Neon Lodging Offers Website looking for new design

We are a online travel discounter based around hotel accommodations in Las Vegas. We need a wordpress design that will be used as our corporate cover page, and also for the affiliate pages. The current design can be viewed at http://postweaveforum.com/clients/neonoffer/ and the final design needs to include most of the navigation components. The affiliate pages will need a space to display the booking engine, for example, as shown at http://www.qrv.travel/marcoti. Our general color scheme is red/black, and the two logos we use are attached.

Because this is a crowded niche it is extremely important that we set ourselves apart in the design. The more visually stunning and out of the box the design, the better. The site needs to look distinctively different than anything else online. Since the overall layout is very basic and does not have to provide a lot of information, it leaves a lot of flexibility in design concepts.

We realize it is a truncated timetable, which is why the increased fee for your time and guaranteed payout.

Industry/Entity Type

Travel

```html
<!DOCTYPE html>
<html lang="en">
<head>
<meta charset="utf-8">
<title>Neon Lodging Offers</title>
<link href="https://fonts.googleapis.com/css2?family=Roboto:wght@300;400;500;700;900&family=Oswald:wght@400;600&display=swap" rel="stylesheet">
<style>
:root{
  --red:#d3121c;
  --red-dark:#a90c14;
  --ink:#1e1e1e;
  --panel:#232323;
  --footer:#262626;
  --footer-bar:#1a1a1a;
  --grey-bg:#ececec;
  --muted:#8c8c8c;
  --line:#d9d9d9;
  --white:#ffffff;
}
*{margin:0;padding:0;box-sizing:border-box}
html,body{width:1200px;height:3737px;overflow:hidden}
body{position:relative;background:var(--grey-bg);font-family:'Roboto',Arial,sans-serif;color:var(--ink)}
.abs{position:absolute}

/* header */
.site-header{left:0;top:0;width:1200px;height:165px;background:var(--white)}
.contact-line{top:22px;font-size:13px;color:#333;display:flex;align-items:center;gap:8px}
.contact-line.address{left:104px}
.contact-line.phone{right:104px;font-weight:700;font-size:15px}
.icon-dot{width:22px;height:22px;border-radius:50%;background:var(--red);display:flex;align-items:center;justify-content:center}
.brand{left:470px;top:18px;width:260px;text-align:center}
.brand-mark{width:60px;height:60px;border-radius:50%;background:var(--red);margin:0 auto 10px}
.brand-name{font-size:17px;font-weight:500;color:var(--ink);letter-spacing:1px}
.main-nav{top:105px;display:flex;gap:40px;font-size:14px;font-weight:500;color:#333;text-transform:uppercase}
.main-nav.left{left:112px}
.main-nav.right{left:755px}
.main-nav .active{color:var(--red);border-bottom:2px solid var(--red);padding-bottom:8px}

/* hero */
.hero{left:0;top:165px;width:1200px;height:497px;background:linear-gradient(180deg,#6d6a98 0%,#c08a74 38%,#7c5343 58%,#2a2220 100%)}
.booking-box{left:364px;top:42px;width:464px;height:330px;background:rgba(255,255,255,.88);padding:28px 34px}
.booking-box h2{font-size:30px;font-weight:400;color:#222;margin-bottom:36px}
.field-row{display:flex;gap:20px;margin-bottom:22px}
.field{flex:1}
.field label{display:block;font-size:11px;color:#777;margin-bottom:6px}
.field span{display:block;height:30px;border:1px solid var(--line);background:var(--white)}
.book-btn{position:absolute;right:150px;bottom:36px;width:96px;height:34px;background:var(--red);color:var(--white);font-size:13px;font-weight:700;display:flex;align-items:center;justify-content:center}

/* search strip */
.search-strip{left:0;top:662px;width:1200px;height:96px;background:var(--ink)}
.search-strip .msg{left:104px;top:13px;width:786px;height:70px;background:var(--white);font-size:19px;font-weight:500;display:flex;align-items:center;padding-left:36px}
.search-strip .cta{left:890px;top:13px;width:207px;height:70px;background:var(--red);color:var(--white);font-size:19px;font-weight:500;display:flex;align-items:center;justify-content:center}

/* about */
.about{left:0;top:758px;width:1200px;height:579px;background:var(--panel);color:var(--white)}
.about h2{top:84px;width:1200px;text-align:center;font-size:22px;font-weight:500;letter-spacing:.5px}
.about .lead{top:122px;left:330px;width:540px;text-align:center;font-size:12px;line-height:19px;color:var(--muted)}
.about-photo{left:290px;top:202px;width:352px;height:282px;background:linear-gradient(135deg,#8f3f48,#d9b9ae 55,#7a6a6c)}
.about-photo .brand-name{position:absolute;left:0;bottom:34px;width:100%;text-align:center;color:#2a2a2a;font-size:26px;font-weight:400;background:rgba(255,255,255,.8);padding:8px 0}
.about .body{left:680px;top:218px;width:300px;font-size:12px;line-height:20px;color:var(--muted)}
.read-more{left:690px;top:440px;width:110px;height:36px;border:1px solid #666;color:var(--white);font-size:11px;font-weight:700;display:flex;align-items:center;justify-content:center}

/* deals */
.deal{overflow:hidden;color:var(--white)}
.deal .more{position:absolute;right:14px;bottom:12px;font-size:12px;font-weight:700}
.deal-night{left:104px;top:1408px;width:278px;height:290px;background:linear-gradient(160deg,#3d3f57,#6a4b4f 60%,#2a2224)}
.deal-night .price{position:absolute;left:40px;top:56px;font-family:'Oswald',sans-serif;font-size:96px;line-height:90px;font-weight:600}
.deal-night .price small{font-size:38px;vertical-align:top}
.deal-night .unit{position:absolute;left:40px;top:150px;font-family:'Oswald',sans-serif;font-size:54px;line-height:56px}
.deal-night .days{position:absolute;left:42px;top:210px;font-family:'Oswald',sans-serif;font-size:22px}
.deal-save{left:390px;top:1408px;width:272px;height:290px;background:linear-gradient(150deg,#6e4a33,#b98a58 50%,#3a2a20)}
.deal-save .tag{position:absolute;left:120px;top:110px;font-family:'Oswald',sans-serif;font-size:22px;line-height:26px}
.deal-save .tag b{font-size:48px;display:block;line-height:52px}
.private-deals{left:683px;top:1408px;width:414px;height:290px;background:var(--white);padding:40px 36px;color:var(--ink)}
.private-deals h3{font-size:30px;font-weight:400;color:var(--red);margin-bottom:14px}
.private-deals p{font-size:11px;line-height:17px;color:#777;text-transform:uppercase;margin-bottom:22px}
.signup{display:flex}
.signup span{flex:1;height:38px;border:1px solid var(--line);font-size:11px;color:#aaa;display:flex;align-items:center;padding-left:12px}
.signup b{width:96px;height:38px;background:var(--red);color:var(--white);font-size:12px;display:flex;align-items:center;justify-content:center}
.deal-offers{left:104px;top:1698px;width:278px;height:282px;background:linear-gradient(180deg,#3a3a3a,#2b2b2b)}
.deal-offers .tag{position:absolute;left:40px;top:110px;font-family:'Oswald',sans-serif;font-size:36px;line-height:40px}
.deal-air{left:390px;top:1698px;width:272px;height:282px;background:linear-gradient(180deg,#9fb8d3,#dfe8f1 55%,#6c8fb3)}
.deal-air .tag{position:absolute;left:120px;top:130px;font-family:'Oswald',sans-serif;font-size:54px;line-height:54px}
.deal-air .tag small{display:block;font-size:14px;line-height:18px;letter-spacing:1px}
.deal-buffet{left:683px;top:1698px;width:414px;height:282px;background:linear-gradient(135deg,#5a3a2a,#b07a52 50%,#4a2c22)}
.deal-buffet .tag{position:absolute;left:150px;top:70px;font-family:'Oswald',sans-serif;font-size:30px;line-height:34px;text-align:center}
.deal-buffet .tag b{display:block;font-size:52px;line-height:56px}

/* rooms */
.rooms{left:104px;top:2030px;width:993px;height:785px;background:var(--white)}
.section-title{font-size:14px;font-weight:700;color:var(--red);text-transform:uppercase}
.rooms .section-title{position:absolute;left:0;top:96px}
.room{position:absolute;width:300px;text-align:center}
.room .photo{height:164px;margin-bottom:22px}
.room h4{font-size:12px;font-weight:700;text-transform:uppercase}
.room .rate{font-size:11px;color:var(--red);margin-top:6px}
.photo.warm{background:linear-gradient(160deg,#7d5a3f,#c9a57a 55%,#4c3526)}
.photo.green{background:linear-gradient(160deg,#4d5f39,#9db07a 50%,#3a3527)}
.photo.blue{background:linear-gradient(160deg,#3e5670,#8aa3b6 50%,#2e3440)}

/* tour operators */
.operators{left:104px;top:2857px;width:993px}
.operator-row{position:absolute;top:55px;left:0;display:flex;gap:28px}
.operator{width:226px;height:108px;background:var(--white);display:flex;align-items:center;justify-content:center;gap:10px;font-size:24px;font-weight:500;color:#333}
.operator i{width:26px;height:26px;border-radius:50%;background:#333;display:block}

/* quote banner */
.quote-banner{left:104px;top:3084px;width:993px;height:136px;background:var(--ink)}
.quote-banner .left{left:0;top:0;width:346px;height:136px;background:linear-gradient(135deg,#2a3442,#7a6146 60%,#1e2430)}
.quote-banner .right{left:640px;top:0;width:353px;height:136px;background:linear-gradient(160deg,#21364c,#6a86b5 50%,#1a1f2c)}
.quote-banner .copy{left:346px;top:0;width:294px;height:136px;text-align:center;color:var(--white);padding-top:24px}
.quote-banner h3{font-size:16px;font-weight:500;margin-bottom:8px}
.quote-banner p{font-size:10px;color:var(--muted);margin-bottom:12px}
.quote-btn{display:inline-block;width:140px;height:36px;line-height:36px;background:var(--red);font-size:13px;font-weight:700}

/* footer */
.site-footer{left:0;top:3270px;width:1200px;height:430px;background:var(--footer);color:#bbb}
.footer-col{position:absolute;top:58px}
.footer-col h5{font-size:15px;font-weight:500;color:var(--white);margin-bottom:18px}
.footer-col p{font-size:12px;line-height:22px}
.socials{display:flex;gap:10px;margin-top:14px}
.socials i{width:22px;height:22px;border-radius:50%;background:#555;display:block}
.socials i:first-child{background:var(--white)}
.help-grid{display:grid;grid-template-columns:200px 200px;gap:14px 16px}
.help-grid span{height:40px;border:1px solid #444;font-size:11px;color:#777;display:flex;align-items:center;padding-left:10px}
.help-grid span.tall{height:94px;grid-row:span 2;align-items:flex-start;padding-top:10px}
.contact-btn{position:absolute;right:0;top:170px;width:120px;height:34px;background:var(--red);color:var(--white);font-size:11px;font-weight:700;display:flex;align-items:center;justify-content:center}
.to-top{left:1110px;top:3660px;width:30px;height:30px;background:var(--red);display:flex;align-items:center;justify-content:center}
.footer-bar{left:0;top:3700px;width:1200px;height:37px;background:var(--footer-bar);color:#888;font-size:11px;display:flex;align-items:center;justify-content:center;gap:40px}
</style>
</head>
<body>

<header class="abs site-header">
  <div class="abs contact-line address">
    <span class="icon-dot"><svg width="10" height="12" viewBox="0 0 10 12"><path d="M5 0a4 4 0 0 0-4 4c0 3 4 8 4 8s4-5 4-8a4 4 0 0 0-4-4zm0 5.5A1.5 1.5 0 1 1 5 2.5a1.5 1.5 0 0 1 0 3z" fill="#fff"/></svg></span>
    4120 S EMBER BLVD #210 LAS VEGAS NV 89119
  </div>
  <div class="abs brand">
    <div class="brand-mark"></div>
    <div class="brand-name">Neon Lodging Offers</div>
  </div>
  <div class="abs contact-line phone">
    <span class="icon-dot"><svg width="11" height="11" viewBox="0 0 12 12"><path d="M2.5 0.5l2 2.5-1.2 1.3a7 7 0 0 0 4.4 4.4L9 7.5l2.5 2-1.3 2A10 10 0 0 1 0.5 1.8z" fill="#fff"/></svg></span>
    +1 702-555-0148
  </div>
  <nav class="abs main-nav left"><span class="active">Home</span><span>About Us</span><span>Groups</span><span>Travel</span></nav>
  <nav class="abs main-nav right"><span>Hotels</span><span>Season Events</span><span>Contact Us</span></nav>
</header>

<section class="abs hero" role="img" aria-label="Resort terrace at dusk overlooking the hills">
  <div class="abs booking-box">
    <h2>Book your room</h2>
    <div class="field-row"><div class="field"><label>Check-in date</label><span></span></div><div class="field"><label>Check-out date</label><span></span></div></div>
    <div class="field-row"><div class="field"><label>Adults</label><span></span></div><div class="field"><label>Children</label><span></span></div><div class="field"><label>Rooms</label><span></span></div></div>
    <div class="book-btn">BOOK</div>
  </div>
</section>

<section class="abs search-strip">
  <div class="abs msg">Get wholesale rates on hotel accommodations with Neon Lodging Offers</div>
  <div class="abs cta">SEARCH EVENTS</div>
</section>

<section class="abs about">
  <h2 class="abs">ABOUT NEON LODGING OFFERS</h2>
  <p class="abs lead">Neon Lodging Offers is a trusted hotel discounter based in Las Vegas. We provide hotel accommodations at wholesale prices for any kind of trip, large or small.</p>
  <div class="abs about-photo" role="img" aria-label="Brand photo with playing card artwork">
    <div class="brand-name">Neon Lodging Offers</div>
  </div>
  <p class="abs body">Our team has booked rooms across the Strip for many years. We compare rates every day, find the best value for each stay and pass the savings to you. Groups, couples and business guests all get fair prices, quick answers and friendly support from the first search to checkout day.</p>
  <div class="abs read-more">READ MORE</div>
</section>

<div class="abs deal deal-night" role="img" aria-label="Night view of the city skyline">
  <div class="price"><small>$</small>89</div>
  <div class="unit">NIGHT</div>
  <div class="days">SUN - THURS</div>
</div>
<div class="abs deal deal-save" role="img" aria-label="Hotel suite interior">
  <div class="tag">SAVE UP TO<b>35%</b></div>
  <span class="more">› MORE</span>
</div>
<div class="abs private-deals">
  <h3>Private Deals</h3>
  <p>Be the first to get our private offers on hotel rooms, shows and weekend stays. Members receive special rates, early booking access and news sent straight to your inbox.</p>
  <div class="signup"><span>Enter your email address</span><b>SIGN UP</b></div>
</div>
<div class="abs deal deal-offers">
  <div class="tag">MORE DEALS<br>&amp; OFFERS</div>
  <span class="more">› MORE</span>
</div>
<div class="abs deal deal-air" role="img" aria-label="Airplane wing above the clouds">
  <div class="tag">AIR<small>HOTEL PACKAGES</small></div>
  <span class="more">› MORE</span>
</div>
<div class="abs deal deal-buffet" role="img" aria-label="Buffet dishes on a table">
  <div class="tag">2 FREE BUFFETS<b>SAVE UP TO 35%</b></div>
  <span class="more">› MORE</span>
</div>

<section class="abs rooms">
  <h3 class="section-title">Highlight Rooms</h3>
  <div class="room" style="left:0;top:120px"><div class="photo warm" role="img" aria-label="Double room with two beds"></div><h4>Double Room Standard</h4><p class="rate">from $86 per night</p></div>
  <div class="room" style="left:346px;top:120px"><div class="photo green" role="img" aria-label="Junior suite with lounge"></div><h4>Junior Suite</h4><p class="rate">from $168 per night</p></div>
  <div class="room" style="left:693px;top:120px"><div class="photo warm" role="img" aria-label="Business room with desk"></div><h4>Business Room Superior</h4><p class="rate">from $146 per night</p></div>
  <div class="room" style="left:0;top:382px"><div class="photo warm" role="img" aria-label="Double room with warm lighting"></div><h4>Double Room Standard</h4><p class="rate">from $86 per night</p></div>
  <div class="room" style="left:346px;top:382px"><div class="photo green" role="img" aria-label="Junior suite bedroom"></div><h4>Junior Suite</h4><p class="rate">from $168 per night</p></div>
  <div class="room" style="left:693px;top:382px"><div class="photo blue" role="img" aria-label="Business room with seating area"></div><h4>Business Room Superior</h4><p class="rate">from $146 per night</p></div>
</section>

<section class="abs operators">
  <h3 class="section-title">Tour Operators</h3>
  <div class="operator-row">
    <div class="operator"><i></i>Linewave</div>
    <div class="operator"><i></i>Soundgrove</div>
    <div class="operator"><i></i>Brightpath</div>
    <div class="operator"><i></i>Codeharbor</div>
  </div>
</section>

<section class="abs quote-banner">
  <div class="abs left" role="img" aria-label="Hotel lobby with lights"></div>
  <div class="abs copy">
    <h3>NEED MORE THAN ONE ROOM?</h3>
    <p>Contact us to ask for group reservations<br>or meeting space</p>
    <span class="quote-btn">GET A QUOTE</span>
  </div>
  <div class="abs right" role="img" aria-label="Concert crowd under stage lights"></div>
</section>

<footer class="abs site-footer">
  <div class="footer-col" style="left:104px">
    <h5>Contact Us Today</h5>
    <p>Name: Lena R. Castell<br>Email: hello@neonlodgingoffers.example<br>Phone: +1 702-555-0148</p>
    <div class="socials"><i></i><i></i><i></i><i></i></div>
  </div>
  <div class="footer-col" style="left:400px">
    <h5>Our Rooms</h5>
    <p>Superior Room<br>Deluxe Room<br>Business Room<br>Executive Suite Room</p>
  </div>
  <div class="footer-col" style="left:694px;width:416px;height:210px">
    <h5>Need Help?</h5>
    <div class="help-grid"><span>Name</span><span class="tall">Message</span><span>Email</span></div>
    <div class="contact-btn">CONTACT US</div>
  </div>
</footer>
<div class="abs to-top"><svg width="12" height="8" viewBox="0 0 12 8"><path d="M1 7l5-5 5 5" stroke="#fff" stroke-width="2" fill="none"/></svg></div>
<div class="abs footer-bar"><span>Terms &amp; Conditions | Privacy Policy</span><span>Copyright © 2015 Neon Lodging Offers. All Rights Reserved.</span></div>

</body>
</html>
```